Gerald Pinnock - Corporate MC & Entertainer

Design a one page A4 flyer
(See Brief Attached)
I'm after a one Page Flyer
A4 Size - One sided
I want the finished artwork in 2 Forms.
1/ One that I could print out myself in a small run ( I have a Dorvan Tint PrintMaster)
or send out as a PDF
2/ A second version that could be printed commercially , so including bleed crop marks so it can be cut to A4 size
I have attached the copy that should be included. (Agency Sweep 2014 WORDS)
If there was too much text to include , we could drop one of the testimonial quotes
I have attached 3 images that could be included if there is room.
If there were too many images I suggest dropping Image 3 ( with bow tie)
As you can see from the copy (or a visit to my website) there are two main services that I provide
Corporate MC Services and Entertainment Services.
These are however intertwined - My MC work often includes some entertaining effects from my ThoughtCatcher Show. I often get booked to MC a conference and provide a show.
I'm after something that is -
Classy , Sophisticated, Smart, perhaps a bit quirky.
Nothing "Magic" like - eg no Rabbits , Wands, puffs of smoke
I have no corporate colour or logo or branding that should be included
You can see some previous flyers here http://www.proflinkora.com/in/geraldpinnock
I like these, but looking for new ideas
Target Market(s)
Corporate , Conference Organisers, Speaker Bureau owners, Large Association Conference committees
Industry/Entity Type
Entertainment
Colors
Designer to choose colors to be used in the design.

```html
<!DOCTYPE html>
<html lang="en">
<head>
<meta charset="utf-8">
<title>Gerald Pinnock – Corporate MC &amp; Entertainer</title>
<link rel="stylesheet" href="https://fonts.googleapis.com/css2?family=Bebas+Neue&family=Open+Sans:wght@400;600;700;800&display=swap">
<style>
  :root{
    --backdrop:#e9e6e1;
    --ink-dark:#1b1c1e;
    --ink-panel:#232427;
    --blue-deep:#0d5f8f;
    --blue-mid:#1f8fc4;
    --blue-bright:#3db8e6;
    --blue-pale:#9fdcf3;
    --white:#ffffff;
    --divider:#2e87b5;
  }
  *{margin:0;padding:0;box-sizing:border-box}
  html,body{width:931px;height:1200px;overflow:hidden;background:var(--backdrop)}
  .canvas{position:relative;width:931px;height:1200px;font-family:"Open Sans",Arial,sans-serif;color:var(--white)}
  .flyer{position:absolute;left:50px;top:47px;width:826px;height:1103px;background:var(--ink-panel);overflow:hidden;box-shadow:0 6px 18px rgba(0,0,0,.35)}
  .masthead{position:absolute;left:0;top:0;width:826px;height:145px;background:linear-gradient(#2b2c2f,#1e1f22)}
  .brand-name{position:absolute;left:30px;top:14px;font-family:"Bebas Neue",Impact,sans-serif;font-size:74px;letter-spacing:1px;line-height:1;
    background:linear-gradient(90deg,var(--blue-deep),var(--blue-bright) 60%,var(--blue-mid));-webkit-background-clip:text;background-clip:text;color:transparent}
  .brand-tagline{position:absolute;left:31px;top:89px;font-size:20.5px;font-weight:600;letter-spacing:.2px;color:var(--white)}
  .hero{position:absolute;left:0;top:143px;width:826px;height:362px}
  .hero svg{position:absolute;left:0;top:0}
  .hero-kicker{position:absolute;left:30px;top:53px;font-weight:800;font-size:20px;line-height:27px;letter-spacing:.3px}
  .hero-headline{position:absolute;left:30px;top:108px;font-family:"Bebas Neue",Impact,sans-serif;line-height:.95;text-shadow:0 3px 5px rgba(0,0,0,.35)}
  .hero-headline .big{display:block;font-size:80px}
  .hero-headline .mid{display:block;font-size:60px}
  .hero-body{position:absolute;left:37px;top:236px;width:370px;font-size:13.5px;line-height:19px;text-transform:uppercase}
  .portrait{position:absolute;left:455px;top:18px;width:371px;height:480px;background:linear-gradient(160deg,#cfd3d6 0%,#8b8f93 25%,#2a2b2e 55%,#151618 100%);clip-path:polygon(18% 0,82% 0,100% 0,100% 100%,0 100%,0 70%)}
  .gallery{position:absolute;top:542px;left:0;width:826px}
  .photo-frame{position:absolute;top:0;width:232px;height:148px;border:3px solid var(--white);border-radius:4px 26px 4px 26px;overflow:hidden}
  .photo-frame div{width:100%;height:100%}
  .f1{left:32px}.f1 div{background:radial-gradient(circle at 45% 45%,#3a4652,#0b0d12 70%)}
  .f2{left:294px}.f2 div{background:radial-gradient(circle at 50% 50%,#2c3a6a,#0a0c14 70%)}
  .f3{left:557px}.f3 div{background:linear-gradient(135deg,#f2f2f2,#d8d8d8 60%,#3a3a3a)}
  .column{position:absolute;top:716px;width:240px}
  .col-head{display:flex;align-items:center;gap:10px;height:42px}
  .col-head h2{font-family:"Bebas Neue",Impact,sans-serif;font-weight:400;font-size:40px;color:var(--blue-bright);line-height:1}
  .col-text{margin-top:20px;font-size:13.5px;line-height:21px;text-transform:uppercase}
  .col-text p+p{margin-top:9px}
  .about{left:30px}
  .world{left:304px}
  .testimonials{left:566px;width:236px}
  .testimonials .col-text{margin-top:14px;text-transform:none;font-size:14px;line-height:21.5px}
  .quote-source{display:block;text-align:right;color:var(--blue-bright);padding-right:6px}
  .quote+.quote{margin-top:9px}
  .divider{position:absolute;top:752px;width:1px;height:300px;background:linear-gradient(var(--divider),rgba(46,135,181,.2))}
  .footer-band{position:absolute;left:0;top:1058px;width:826px;height:45px;background:linear-gradient(90deg,var(--blue-deep),var(--blue-mid) 30%,var(--blue-mid) 70%,var(--blue-deep));display:flex;align-items:center;justify-content:center;font-weight:700;font-size:21px;letter-spacing:.2px}
</style>
</head>
<body>
<div class="canvas">
  <div class="flyer">
    <header class="masthead">
      <div class="brand-name">GERALD PINNOCK</div>
      <div class="brand-tagline">AUSTRALIA'S MAGICIAN OF THE MIND</div>
    </header>

    <section class="hero">
      <svg width="826" height="362" viewBox="0 0 826 362" aria-hidden="true">
        <defs>
          <linearGradient id="heroBlue" x1="0" y1="0" x2="1" y2="0.4">
            <stop offset="0" stop-color="#0f5f8e"/>
            <stop offset="0.55" stop-color="#2a9dd0"/>
            <stop offset="1" stop-color="#1a7fb4"/>
          </linearGradient>
        </defs>
        <path d="M0 0 H826 V332 C600 300 300 330 0 340 Z" fill="url(#heroBlue)"/>
        <path d="M0 330 C300 322 600 292 826 322 V332 C600 300 300 330 0 340 Z" fill="#7fd0f0" opacity=".7"/>
        <path d="M0 340 C300 330 600 300 826 332 V362 H0 Z" fill="#232427"/>
      </svg>
      <div class="hero-kicker">CORPORATE MC &amp; ENTERTAINER<br>SOLVING YOUR CONFERENCE PUZZLES!</div>
      <h1 class="hero-headline"><span class="big">IN THE LAST TWO</span><span class="mid">YEARS GERALD</span></h1>
      <p class="hero-body">HAS BEEN ENGAGED AS THE CONFERENCE MC FOR EVENTS IN HAWAII, NEW ZEALAND, HONG KONG &amp; ALL STATES OF AUSTRALIA.</p>
    </section>
    <div class="portrait" role="img" aria-label="Portrait of the entertainer in a tuxedo and bow tie, smiling"></div>

    <section class="gallery">
      <div class="photo-frame f1"><div role="img" aria-label="Photo of the MC speaking on stage against a starry backdrop"></div></div>
      <div class="photo-frame f2"><div role="img" aria-label="Photo of the entertainer performing on stage with arms outstretched"></div></div>
      <div class="photo-frame f3"><div role="img" aria-label="Head-and-shoulders photo of the entertainer on a white background"></div></div>
    </section>

    <section class="column about">
      <div class="col-head">
        <svg width="44" height="40" viewBox="0 0 44 40" aria-hidden="true"><g fill="#fff"><circle cx="22" cy="11" r="9"/><circle cx="11" cy="20" r="9"/><circle cx="33" cy="20" r="9"/><circle cx="22" cy="29" r="9"/></g><circle cx="22" cy="20" r="3" fill="#232427"/></svg>
        <h2>ABOUT HIM</h2>
      </div>
      <div class="col-text"><p>HE FACILITATED 24 AUSTRALIAN MAJOR PROJECT CONFERENCES FOR FAIRVEX AND 16 INTERNATIONAL CEO SUMMITS FOR MERIDALE SUMMITS.</p></div>
    </section>
    <div class="divider" style="left:283px"></div>

    <section class="column world">
      <div class="col-head">
        <svg width="40" height="40" viewBox="0 0 40 40" aria-hidden="true"><circle cx="20" cy="20" r="18" fill="none" stroke="#fff" stroke-width="2.5"/><path d="M13 11 L30 20 L13 29 L18 20 Z" fill="#fff"/></svg>
        <h2>ABOUT WORLD</h2>
      </div>
      <div class="col-text">
        <p>IN THE AUSTRALIAN CORPORATE SECTOR, HE MANAGED MAJOR EVENTS FOR - OZBROKERAGE, IBRC, HOMEWELL CARE, SIGNAL HIRE, PARISHCARE AND THE GROVE &amp; GARDEN GUILD.</p>
        <p>AS AN ENTERTAINER HE CRUISED THE WORLD ON SEVERAL LUXURY CRUISE SHIPS, VISITING JAPAN, KOREA, CHINA, TAHITI AND NEW ZEALAND IN HIS TRAVELS.</p>
      </div>
    </section>
    <div class="divider" style="left:553px"></div>

    <section class="column testimonials">
      <div class="col-head">
        <svg width="40" height="40" viewBox="0 0 40 40" aria-hidden="true"><g fill="none" stroke="#fff" stroke-width="2"><circle cx="20" cy="20" r="18"/><ellipse cx="20" cy="20" rx="8" ry="18"/><line x1="20" y1="2" x2="20" y2="38"/><line x1="2" y1="20" x2="38" y2="20"/><path d="M5 11 H35 M5 29 H35"/></g></svg>
        <h2>TESTIMONIALS</h2>
      </div>
      <div class="col-text">
        <p class="quote">"A big thank you for a really good job on Friday night which was carried out with aplomb - well done!"<span class="quote-source">- Grove &amp; Garden Guild</span></p>
        <p class="quote">"Huge thanks for your professionalism with the Awards, getting a laugh from everyone and in general creating an atmosphere that was enjoyable and relaxed!"<span class="quote-source">- Homewell Care</span></p>
      </div>
    </section>

    <footer class="footer-band">www.proflinkora.com/in/geraldpinnock</footer>
  </div>
</div>
</body>
</html>
```